Design a New Site for a very cool Watch

We have the overall design element of the website and the banners in the PSD file. We need someone to finish our design in PSD and than convert to HTML. We have included the instructions, PSD file, images and all text.

We currently use Hubspot to host and make changes to our site. The entire design aspect is complete so all we need is some minor changes and additions within the photoshop design and than the coding into HTML.

Please only sign up if you understand photoshop and HTML conversion

Here is the DropBox link to the files
https://files.quorvel-share.net/s/pm4kx82lwq7dtne/Belthor%20Site.zip
Updates

We have the basic design concept in Photoshop.  We just need someone who can complete some changes, make some additions and convert to HTML

Target Market(s)

Watch Buyers

Requirements
Must have
• Must look like a professional luxury brand

Our brand colors are very basic with Black, White and Grey can be used

```html
<!DOCTYPE html>
<html lang="en">
<head>
<meta charset="utf-8">
<title>Belthor &amp; Co. — The Lyra Watch</title>
<link rel="stylesheet" href="https://fonts.googleapis.com/css2?family=Gelasio:ital,wght@0,400;1,400&family=Source+Sans+3:wght@600&display=swap">
<style>
  :root {
    --night: #05070f;
    --slate: #2c3447;
    --slate-top: #5a6378;
    --logo-panel: #525a70;
    --ice: #b9c5e2;
    --ice-soft: #c9d2e6;
    --white: #ffffff;
    --footer-text: #3a4562;
    --serif: "Gelasio", Georgia, serif;
    --sans: "Source Sans 3", Arial, sans-serif;
  }
  * { margin: 0; padding: 0; box-sizing: border-box; }
  html, body { width: 1200px; height: 1162px; overflow: hidden; background: var(--night); }
  .page { position: relative; width: 1200px; height: 1162px; font-family: var(--serif); }

  .top-band {
    position: absolute; left: 0; top: 0; width: 1200px; height: 132px;
    background: radial-gradient(circle at 12% 60%, #6c7590 0, transparent 90px),
                radial-gradient(circle at 88% 50%, #6a738c 0, transparent 100px),
                linear-gradient(180deg, #646d84, var(--slate-top));
  }

  .brand-panel {
    position: absolute; left: 502px; top: 0; width: 196px; height: 194px;
    background: var(--logo-panel); border-bottom: 3px solid var(--white);
    display: flex; flex-direction: column; align-items: center; justify-content: flex-end;
    padding-bottom: 22px; z-index: 2;
  }
  .brand-panel .mark { width: 14px; height: 14px; border: 2px solid var(--white); margin-bottom: 14px; }
  .brand-name { font-family: var(--serif); color: var(--white); font-size: 19px; letter-spacing: 0.5px; }
  .notch {
    position: absolute; left: 50%; bottom: -10px; transform: translateX(-50%);
    width: 0; height: 0; border-left: 6px solid transparent; border-right: 6px solid transparent;
    border-top: 7px solid var(--white);
  }

  .hero { position: absolute; left: 0; top: 132px; width: 1200px; height: 600px; background: var(--night); }
  .moon-photo {
    position: absolute; left: 186px; top: 84px; width: 344px; height: 430px;
    border-radius: 50%;
    background: radial-gradient(ellipse at 60% 45%, #dfe6f4 0, #a9b6cf 45%, #6b7894 80%, #1a2030 100%);
  }
  .hero-copy { position: absolute; left: 576px; top: 148px; width: 492px; text-align: center; color: var(--ice); }
  .rule { display: block; width: 100%; height: 12px; }
  .hero-title { font-style: italic; font-weight: 400; font-size: 26px; line-height: 28px; margin-top: 28px; letter-spacing: 0.3px; }
  .hero-lead { font-style: italic; font-size: 15px; margin-top: 26px; }
  .hero-text { font-style: italic; font-size: 15px; line-height: 27px; margin-top: 28px; margin-bottom: 22px; }
  .learn-more {
    position: absolute; left: 743px; top: 436px; width: 159px; height: 43px;
    border: 1px dotted #5a6478; color: var(--ice-soft);
    font-family: var(--sans); font-weight: 600; font-size: 19px; letter-spacing: 0.3px;
    display: flex; align-items: center; justify-content: center; text-decoration: none;
  }

  .lower { position: absolute; left: 0; top: 732px; width: 1200px; height: 372px; background: var(--slate); }
  .lower .rule { position: absolute; left: 132px; top: 14px; width: 936px; }
  .menu { position: absolute; left: 132px; top: 36px; width: 936px; list-style: none; }
  .menu-item { position: relative; height: 57px; border-bottom: 3px solid var(--white); }
  .menu-item + .menu-item { margin-top: 0; }
  .menu-bg { position: absolute; inset: 0; }
  .menu-item a {
    position: relative; display: flex; align-items: center; justify-content: center; height: 100%;
    color: var(--ice-soft); font-style: italic; font-size: 22px; text-decoration: none; letter-spacing: 0.2px;
  }
  .menu-item .notch { bottom: -10px; border-top-color: var(--white); z-index: 1; }
  .bg-story { background: linear-gradient(90deg, #3d4660, #7a849c 45%, #5b647c); }
  .bg-register { background: linear-gradient(90deg, #101a33, #2c3a5e 40%, #0f1a34); }
  .bg-repair { background: linear-gradient(90deg, #1a2440, #2d3a5a 50%, #4b5672); }
  .bg-subscribe { background: linear-gradient(90deg, #0d1630, #24407a 35%, #0b1328); }
  .bg-spread { background: linear-gradient(90deg, #0c1020, #1b2133 50%, #0c1020); }

  .footer { position: absolute; left: 0; top: 1104px; width: 1200px; height: 58px; background: var(--night);
    display: flex; align-items: center; justify-content: center; }
  .copyright { color: var(--footer-text); font-size: 11px; }
</style>
</head>
<body>
<div class="page">
  <header>
    <div class="top-band" role="img" aria-label="Faint photograph of cut gemstones on a grey field"></div>
    <div class="brand-panel">
      <span class="mark"></span>
      <span class="brand-name">BELTHOR &amp; CO.</span>
      <span class="notch"></span>
    </div>
  </header>

  <section class="hero">
    <div class="moon-photo" role="img" aria-label="Photograph of the gibbous moon"></div>
    <div class="hero-copy">
      <svg class="rule" viewBox="0 0 492 12" aria-hidden="true">
        <line x1="2" y1="6" x2="236" y2="6" stroke="#c9d2e6" stroke-width="2" stroke-linecap="round" stroke-dasharray="0 6"/>
        <line x1="256" y1="6" x2="490" y2="6" stroke="#c9d2e6" stroke-width="2" stroke-linecap="round" stroke-dasharray="0 6"/>
        <rect x="241" y="1" width="7" height="7" fill="#ffffff" transform="rotate(45 246 6)"/>
      </svg>
      <h1 class="hero-title">HOW DID WE PUT THE UNIVERSE<br>IN THE LYRA WATCH</h1>
      <p class="hero-lead">Over the years....</p>
      <p class="hero-text">A small amount of fragments from the Moon, Mars and the other rare<br>celestial treasures from the universe have fallen to the Earth.</p>
      <svg class="rule" viewBox="0 0 492 12" aria-hidden="true">
        <line x1="2" y1="6" x2="236" y2="6" stroke="#c9d2e6" stroke-width="2" stroke-linecap="round" stroke-dasharray="0 6"/>
        <line x1="256" y1="6" x2="490" y2="6" stroke="#c9d2e6" stroke-width="2" stroke-linecap="round" stroke-dasharray="0 6"/>
        <rect x="241" y="1" width="7" height="7" fill="#ffffff" transform="rotate(45 246 6)"/>
      </svg>
    </div>
    <a class="learn-more" href="#">LEARN MORE</a>
  </section>

  <nav class="lower">
    <svg class="rule" viewBox="0 0 936 12" aria-hidden="true">
      <line x1="2" y1="6" x2="458" y2="6" stroke="#c9d2e6" stroke-width="2" stroke-linecap="round" stroke-dasharray="0 6"/>
      <line x1="478" y1="6" x2="934" y2="6" stroke="#c9d2e6" stroke-width="2" stroke-linecap="round" stroke-dasharray="0 6"/>
      <rect x="463" y="1" width="8" height="8" fill="#ffffff" transform="rotate(45 468 6)"/>
    </svg>
    <ul class="menu">
      <li class="menu-item"><div class="menu-bg bg-story" role="img" aria-label="Close-up of the lunar surface"></div><a href="#">THE LYRA STORY</a><span class="notch"></span></li>
      <li class="menu-item"><div class="menu-bg bg-register" role="img" aria-label="Watch hands over a crystal dial"></div><a href="#">REGISTER YOUR WATCH</a><span class="notch"></span></li>
      <li class="menu-item"><div class="menu-bg bg-repair" role="img" aria-label="Faceted crystal and watch hands"></div><a href="#">REPAIR, MAINTENANCE &amp; WARRANTY</a><span class="notch"></span></li>
      <li class="menu-item"><div class="menu-bg bg-subscribe" role="img" aria-label="Earth horizon glowing in blue"></div><a href="#">SUBSCRIBE</a><span class="notch"></span></li>
      <li class="menu-item"><div class="menu-bg bg-spread" role="img" aria-label="Dark gemstone texture"></div><a href="#">SPREAD THE WORDS</a><span class="notch"></span></li>
    </ul>
  </nav>

  <footer class="footer">
    <p class="copyright">Copyright 2013 Belthor &amp; Co.</p>
  </footer>
</div>
</body>
</html>
```